RTV ELECTRICAL GROUP Website Providing Electrical Services

We're a company providing electrical services to the public. We're located in Bankstown a suburb in Sydney, Australia. We are a team of 4 electricians that provide service work to the public. We work on new construction buildings such as single story, double story & units. We also do office fit outs & commercial factory work.

Target Market(s)

All Age Groups
Construction People
Sydney, Australia

Industry/Entity Type

Electrical

Contact Information for Business Card

Name Gavin Lorrimer
Contact Number 0481 502 743
Company License 904517B
ABN 53 204 871 365
Residential Commercial Industrial
info@rtvelectrical.example.com.au

Coding

Coded - Design and coding required

Number of Pages Required

5+ page

Font styles to use
Serif
Sans Serif

Colors

Designer to choose colors to be used in the design.

Requirements
Must have
• WORDPRESS
• Nice & Simple
• Eye catching
• Easy to Read
• Contact details
• Instagram Linked
• Facebook Page Linked
• All Social Media Linked
• Live Chat
• Form Submission
• Testimonial
• Specify services Offered
• About Us (Company details)
• Industrial Installation Page
• Residential Installation Page
• Commercial Installation Page
• Mode of payment (cash, credit-debit card, cheque)
• Local & national electrical news
• Project Videos
• Newsletter
• Level 2 licensed accredited
• Project pictures and articles
• Awards
• Legalities (company's policy, terms, rules)
• FAQ's (Frequently asked questions)
• Collaboration Projects
• Careers
• Projects
• Suppliers
• Customer Perks (discounts or freebies)
• Employees Informations (pictures and basic information)
• Opening Hours and Map location
• Company Logo & Company License (owner license)
• Accreditation
• Customer Service
• Safety/Safety tips
• Clients information (regular clients)
• Expertise
• Company's processes
• Timeline page
• Homepage
• Specify installations
• Search toolbar
• Portfolio
• Request for an appointment - servicing
• Feedbacks
Nice to have
• Articles (better if recent project articles)
• Advertisement
• Influencer Quote
• Sneak Peeks (if you have new services offered)
• Staff Highlights
• Job Hiring (Career Growth)
• Ratings (Rate our service)
• A day/week in the work
• Personal Anecdotes
• Before and after post projects
• Ecological Values
• Marketing feature
• Tagline
• Streaming interactive videos
• Timeline
• Calendar
• Blog
• Emergency Services/Hotline
• Additional services offered
• Transportation (vehicle - car images of our company)
• Comment box (company - clients)
• Rate Us (Performance rating)
Should not have
• Website shouldn't be dark
• Website shouldn't be hard to read
• Advertisement of competitors
• Moving objects
• Dark background

```html
<!DOCTYPE html>
<html lang="en">
<head>
<meta charset="utf-8">
<title>RTV Electrical Group</title>
<link href="https://fonts.googleapis.com/css2?family=Roboto:wght@400;500;700&display=swap" rel="stylesheet">
<style>
:root{
  --blue:#1c6aa6;
  --blue-dark:#155a8e;
  --blue-bright:#2a8fd0;
  --ink:#222;
  --muted:#8a8a8a;
  --soft:#f7f7f7;
  --white:#fff;
  --footer:#1b1b1b;
  --field:#4a4a4a;
}
*{margin:0;padding:0;box-sizing:border-box}
html,body{width:1200px;height:2844px;overflow:hidden}
body{position:relative;font-family:'Roboto',Arial,sans-serif;color:var(--ink);background:var(--white)}
.abs{position:absolute}
.center{left:0;width:1200px;text-align:center}

/* hero */
.hero{left:0;top:0;width:1200px;height:586px;background:linear-gradient(100deg,#6b6b6b 0%,#8d8d8d 35%,#7a7774 60%,#5e5a56 100%)}
.hero-shade{left:0;top:0;width:1200px;height:586px;background:rgba(0,0,0,.25)}
.nav a{position:absolute;top:42px;color:var(--white);font-size:13px;font-weight:500;text-decoration:none;letter-spacing:.3px}
.brand{left:521px;top:0;width:156px;height:95px;background:var(--white);box-shadow:0 2px 8px rgba(0,0,0,.2);display:flex;flex-direction:column;align-items:center;justify-content:center;gap:6px}
.brand-mark{width:26px;height:26px;border-radius:50%;background:var(--blue)}
.brand-name{font-size:11px;font-weight:500;color:var(--blue);letter-spacing:.4px;text-align:center;line-height:1.3}
.hero-title{left:0;top:226px;width:1200px;text-align:center;color:var(--white);font-size:27px;font-weight:700}
.hero-text{left:0;top:272px;width:1200px;text-align:center;color:var(--white);font-size:15px;line-height:19px}
.btn-quote{left:521px;top:343px;width:150px;height:46px;border:1px solid var(--white);color:var(--white);font-size:16px;display:flex;align-items:center;justify-content:center}
.live-chat{left:1158px;top:241px;width:42px;height:148px;background:var(--blue-bright);border-radius:6px 0 0 6px;color:var(--white)}
.live-chat span{position:absolute;left:13px;top:96px;transform:rotate(-90deg);transform-origin:left top;font-size:12px;font-weight:700;white-space:nowrap}
.live-chat svg{position:absolute;left:11px;top:106px}

.down{width:42px;height:42px;border-radius:50%;background:var(--blue);display:flex;align-items:center;justify-content:center;z-index:3}

/* section titles */
.sec-title{font-size:19px;font-weight:700;color:var(--ink)}
.sec-sub{font-size:15px;color:var(--muted);line-height:19px}

/* services */
.cable{left:0;top:716px;width:226px;height:300px;background:linear-gradient(155deg,#f4f4f4 0%,#e6e6e6 45%,#d9d9d9 100%)}
.service-line{top:796px;left:309px;width:571px;border-top:1px dashed #ccc}
.service{width:180px;text-align:center}
.service-icon{width:102px;height:102px;border-radius:50%;border:1px dashed #c8c8c8;background:var(--white);margin:0 auto;display:flex;align-items:center;justify-content:center}
.service p{margin-top:27px;font-size:13px;color:#666;line-height:18px}
.vline{left:599px;width:0;border-left:1px solid #ccc}

/* team */
.team-bg{left:0;top:1016px;width:1200px;height:491px;background:var(--soft)}
.member{top:1183px;width:200px;height:186px;background:var(--white);box-shadow:0 1px 3px rgba(0,0,0,.08)}
.member-photo{width:184px;height:154px}
.member-name{text-align:center;font-size:14px;color:#444;margin-top:10px}
.tools{left:986px;top:1372px;width:214px;height:135px;background:linear-gradient(135deg,#f2d4d4 0%,#e26166 55%,#c8262e 100%)}

/* testimonial */
.testimonial{left:0;top:1507px;width:1200px;height:427px;background:linear-gradient(90deg,#4e3d3d 0%,#6a5858 50%,#4a3a3a 100%)}
.quote-text{left:150px;top:1662px;width:900px;text-align:center;color:var(--white);font-size:14px;font-style:italic;line-height:19px}
.btn-more{left:523px;top:1828px;width:150px;height:45px;border:1px solid #8fc3ea;color:var(--white);font-size:14px;font-weight:700;display:flex;align-items:center;justify-content:center}

/* projects */
.project-card{left:161px;top:2110px;width:431px;height:345px;border:1px solid #ddd;background:var(--white)}
.project-hand{left:0;top:20px;width:185px;height:324px;background:linear-gradient(160deg,#f3f3f3 0%,#e8c8b4 55%,#d8a98e 100%)}
.project-card h3{position:absolute;left:209px;top:62px;font-size:15px;font-weight:700;line-height:20px;color:var(--ink)}
.project-card p{position:absolute;left:209px;width:200px;font-size:11px;color:#777;line-height:19px}
.btn-outline{position:absolute;left:209px;top:272px;width:98px;height:40px;border:2px solid var(--blue-bright);border-radius:20px;color:var(--blue);font-size:12px;font-weight:700;display:flex;align-items:center;justify-content:center}
.tile{width:212px;height:165px}
.tile-label{position:absolute;color:var(--white);font-size:14px;font-weight:700;letter-spacing:.5px}

/* footer */
.footer{left:0;top:2544px;width:1200px;height:262px;background:var(--footer);color:var(--white)}
.foot-head{font-size:13px;font-weight:500;color:#ddd;letter-spacing:.5px}
.foot-line{font-size:11px;font-weight:700;color:var(--white)}
.foot-nav{font-size:11px;color:#ccc;line-height:19px;list-style:none}
.foot-nav .active{color:#2a9be0}
.field{background:var(--field);color:#bbb;font-size:10px;padding:6px 8px}
.btn-send{left:675px;top:2745px;width:110px;height:42px;border:2px solid var(--white);border-radius:21px;color:var(--white);font-size:11px;font-weight:700;display:flex;align-items:center;justify-content:center}
.bottom-bar{left:0;top:2806px;width:1200px;height:38px;background:var(--blue-dark);color:var(--white);font-size:10px;font-weight:700}
.social{width:22px;height:22px;border-radius:50%;border:1.5px solid var(--white)}
</style>
</head>
<body>

<!-- hero -->
<div class="abs hero" role="img" aria-label="Electrician in hard hat working on a switchboard"></div>
<div class="abs hero-shade"></div>
<nav class="nav">
  <a style="left:159px">HOME</a>
  <a style="left:231px">ABOUT US</a>
  <a style="left:330px">OUR SERVICES</a>
  <a style="left:753px">PROJECTS</a>
  <a style="left:855px">TESTIMONIAL</a>
  <a style="left:976px">CONTACT</a>
</nav>
<div class="abs brand"><span class="brand-mark"></span><span class="brand-name">RTV ELECTRICAL GROUP</span></div>
<h1 class="abs hero-title">WELCOME TO RTV ELECTRICAL</h1>
<p class="abs hero-text">Lorem ipsum dolor sit amet, consectetur adipiscing elit, sed do<br>eiusmod tempor incididunt ut labore et dolore magna aliqua.</p>
<div class="abs btn-quote">Book a Quote</div>
<div class="abs live-chat"><span>LIVE CHAT</span><svg width="20" height="20" viewBox="0 0 20 20"><path d="M3 4h14v9H8l-4 3v-3H3z" fill="none" stroke="#fff" stroke-width="1.5"/></svg></div>

<div class="abs down" style="left:579px;top:565px"><svg width="20" height="20" viewBox="0 0 20 20"><circle cx="10" cy="10" r="8" fill="none" stroke="#fff" stroke-width="1.5"/><path d="M10 5v9M6.5 10.5 10 14l3.5-3.5" fill="none" stroke="#fff" stroke-width="1.5"/></svg></div>

<!-- services -->
<div class="abs cable" role="img" aria-label="Stripped electrical cables with coloured wires"></div>
<h2 class="abs center sec-title" style="top:668px">RTV ELECTRICAL SERVICES</h2>
<div class="abs service-line"></div>
<div class="abs service" style="left:219px;top:745px"><div class="service-icon"><svg width="30" height="36" viewBox="0 0 30 36"><path d="M18 2 4 21h10l-3 13 15-20H16z" fill="none" stroke="#444" stroke-width="2" stroke-linejoin="round"/></svg></div><p>Lorem ipsum dolor<br>sit amet,</p></div>
<div class="abs service" style="left:410px;top:745px"><div class="service-icon"><svg width="30" height="36" viewBox="0 0 30 36"><path d="M18 2 4 21h10l-3 13 15-20H16z" fill="none" stroke="#444" stroke-width="2" stroke-linejoin="round"/></svg></div><p>Lorem ipsum dolor<br>sit amet,</p></div>
<div class="abs service" style="left:600px;top:745px"><div class="service-icon"><svg width="30" height="36" viewBox="0 0 30 36"><path d="M18 2 4 21h10l-3 13 15-20H16z" fill="none" stroke="#444" stroke-width="2" stroke-linejoin="round"/></svg></div><p>Lorem ipsum dolor<br>sit amet,</p></div>
<div class="abs service" style="left:790px;top:745px"><div class="service-icon"><svg width="30" height="36" viewBox="0 0 30 36"><path d="M18 2 4 21h10l-3 13 15-20H16z" fill="none" stroke="#444" stroke-width="2" stroke-linejoin="round"/></svg></div><p>Lorem ipsum dolor<br>sit amet,</p></div>
<div class="abs vline" style="top:920px;height:75px"></div>

<!-- team -->
<div class="abs team-bg"></div>
<div class="abs down" style="left:579px;top:995px"><svg width="20" height="20" viewBox="0 0 20 20"><circle cx="10" cy="10" r="8" fill="none" stroke="#fff" stroke-width="1.5"/><path d="M10 5v9M6.5 10.5 10 14l3.5-3.5" fill="none" stroke="#fff" stroke-width="1.5"/></svg></div>
<h2 class="abs center sec-title" style="top:1070px">OUR TEAM</h2>
<p class="abs center sec-sub" style="top:1105px">Lorem ipsum dolor sit amet, consectetur adipiscing elit,<br>sed do eiusmod tempor incididunt ut labore et dolore magna aliqua.</p>
<div class="abs member" style="left:173px"><div class="member-photo" role="img" aria-label="Team member working on a switchboard" style="background:linear-gradient(135deg,#c98a4a,#3d5f8c)"></div><p class="member-name">Liam Harcourt</p></div>
<div class="abs member" style="left:389px"><div class="member-photo" role="img" aria-label="Team member holding a drill" style="background:linear-gradient(135deg,#e8e8e8,#2f4a6e)"></div><p class="member-name">Owen Keller</p></div>
<div class="abs member" style="left:607px"><div class="member-photo" role="img" aria-label="Team member with tool belt" style="background:linear-gradient(135deg,#dcdcdc,#a0453c)"></div><p class="member-name">Dylan Marsh</p></div>
<div class="abs member" style="left:823px"><div class="member-photo" role="img" aria-label="Team member in front of brick wall" style="background:linear-gradient(135deg,#8a5a42,#b24a3a)"></div><p class="member-name">Noah Whitby</p></div>
<div class="abs vline" style="top:1410px;height:80px"></div>
<div class="abs tools" role="img" aria-label="Red pliers and insulation tape"></div>

<!-- testimonial -->
<div class="abs testimonial" role="img" aria-label="Gloved hands fitting a wall power outlet"></div>
<div class="abs down" style="left:579px;top:1486px"><svg width="20" height="20" viewBox="0 0 20 20"><circle cx="10" cy="10" r="8" fill="none" stroke="#fff" stroke-width="1.5"/><path d="M10 5v9M6.5 10.5 10 14l3.5-3.5" fill="none" stroke="#fff" stroke-width="1.5"/></svg></div>
<h2 class="abs center sec-title" style="top:1559px;color:var(--white)">WHAT OUR CLIENT SAYS</h2>
<svg class="abs" style="left:580px;top:1605px" width="40" height="34" viewBox="0 0 40 34"><path d="M2 32V18C2 8 7 3 16 2v6c-5 1-7 4-7 9h7v15zM23 32V18c0-10 5-15 14-16v6c-5 1-7 4-7 9h7v15z" fill="#fff"/></svg>
<p class="abs quote-text">Lorem ipsum dolor sit amet, consectetur adipiscing elit, sed do eiusmod tempor incididunt ut labore et dolore magna aliqua.<br>Ut enim ad minim veniam, quis nostrud exercitation ullamco laboris nisi ut aliquip ex ea commodo consequat. Duis aute<br>irure dolor in reprehenderit in voluptate velit esse cillum dolore eu fugiat nulla pariatur.</p>
<div class="abs" style="left:599px;top:1772px;height:56px;border-left:1px dashed #ccc"></div>
<div class="abs btn-more">VIEW MORE</div>

<!-- projects -->
<h2 class="abs center sec-title" style="top:1993px">OUR COMPLETED PROJECTS</h2>
<p class="abs center sec-sub" style="top:2028px">Lorem ipsum dolor sit amet, consectetur adipiscing elit,<br>sed do eiusmod tempor incididunt ut labore et dolore magna aliqua.</p>
<div class="abs project-card">
  <div class="abs project-hand" role="img" aria-label="Hand holding a power plug"></div>
  <h3>RTV Electrical Completed<br>Projects</h3>
  <p style="top:115px">Lorem ipsum dolor sit amet, con-<br>sectetur adipiscing elit,</p>
  <p style="top:170px">sed do eiusmod tempor incididunt<br>ut labore et dolore magna aliqua.<br>Ut enim ad minim veniam,</p>
  <div class="btn-outline">MORE</div>
</div>
<div class="abs tile" style="left:603px;top:2110px;background:linear-gradient(135deg,#b9c6d3,#d96a3c)" role="img" aria-label="Electrician working at an office switchboard"><span class="tile-label" style="left:14px;top:12px">OFFICE</span></div>
<div class="abs tile" style="left:829px;top:2110px;background:linear-gradient(135deg,#f1f1f1,#2e5f99)" role="img" aria-label="Electrician holding coiled blue cable"><span class="tile-label" style="right:12px;bottom:12px;color:#222">COMMERCIAL</span></div>
<div class="abs tile" style="left:603px;top:2292px;background:linear-gradient(135deg,#d6c9c2,#6b3b34)" role="img" aria-label="Hands installing a house power socket"><span class="tile-label" style="right:12px;bottom:12px">HOUSE</span></div>
<div class="abs tile" style="left:829px;top:2292px;background:linear-gradient(135deg,#eef2f6,#2a4f8a)" role="img" aria-label="Electrician in blue hard hat with pliers"><span class="tile-label" style="right:12px;top:12px;color:#222">GENERAL</span></div>

<!-- footer -->
<footer class="abs footer">
  <svg class="abs" style="left:161px;top:25px" width="12" height="16" viewBox="0 0 12 16"><path d="M6 0a6 6 0 0 0-6 6c0 4.5 6 10 6 10s6-5.5 6-10a6 6 0 0 0-6-6zm0 8.5A2.5 2.5 0 1 1 6 3.5a2.5 2.5 0 0 1 0 5z" fill="#ddd"/></svg>
  <p class="abs foot-head" style="left:179px;top:28px">CONTACT US</p>
  <p class="abs foot-line" style="left:161px;top:70px">Tel: 0481 502 743</p>
  <p class="abs foot-line" style="left:161px;top:98px">Fax: 02 9790 4418</p>
  <p class="abs foot-line" style="left:161px;top:126px">P.O.Box: 58213</p>
  <svg class="abs" style="left:161px;top:154px" width="24" height="24" viewBox="0 0 24 24"><circle cx="12" cy="12" r="11" fill="none" stroke="#2a9be0" stroke-width="1.5"/><rect x="6.5" y="8" width="11" height="8" fill="none" stroke="#2a9be0" stroke-width="1.3"/><path d="M6.5 8 12 12.5 17.5 8" fill="none" stroke="#2a9be0" stroke-width="1.3"/></svg>
  <p class="abs foot-line" style="left:195px;top:160px">E-mail: info@rtvelectrical.example.com.au</p>

  <p class="abs foot-head" style="left:413px;top:28px">NAVIGATION</p>
  <ul class="abs foot-nav" style="left:413px;top:60px">
    <li class="active">- Home</li>
    <li>- About Us</li>
    <li>- Our Services</li>
    <li>- Completed Projects</li>
    <li>- Testimonials</li>
    <li>- Contact Us</li>
  </ul>

  <p class="abs foot-head" style="left:675px;top:28px">SUBMISSION FORM</p>
  <div class="abs field" style="left:675px;top:63px;width:178px;height:32px">Name</div>
  <div class="abs field" style="left:859px;top:63px;width:180px;height:32px">Email ID</div>
  <div class="abs field" style="left:675px;top:105px;width:364px;height:83px">Message</div>
</footer>
<div class="abs btn-send">SEND</div>

<div class="abs bottom-bar">
  <p class="abs" style="left:161px;top:12px">Copyright © 2018 RTV Electrical &nbsp;-&nbsp; All Rights Reserved &nbsp;-&nbsp; Privacy Policy &nbsp;-&nbsp; Terms of Service</p>
  <div class="abs social" style="left:955px;top:8px"></div>
  <div class="abs social" style="left:984px;top:8px"></div>
  <div class="abs social" style="left:1013px;top:8px"></div>
</div>

</body>
</html>
```